Website Design for Kindred Harbor Network

Please design and code a new website.
Here are the sites I like best:
http://www.voyaglint.com/alternate/
http://www.wheelsbrevant.org
Please make it similar but look at the competitor site (below) for images and wording. This is NOT a car donation site. It's a senior lead placement site like https://www.elderbrookhaven.com. I just like this sites above as a lead generation sites.
Competitor site:
https://www.elderbrookhaven.com (use ideas / verbiage from this site)
Updates
Competitor site:

```html
<!DOCTYPE html>
<html lang="en">
<head>
<meta charset="utf-8">
<title>Kindred Harbor Network</title>
<link href="https://fonts.googleapis.com/css2?family=Roboto:wght@400;500;700;900&display=swap" rel="stylesheet">
<style>
:root{
  --gold:#c39a3e;
  --gold-dark:#a8822f;
  --ink:#222;
  --text:#666;
  --dark:#24281f;
  --dark-2:#2d3228;
  --dark-3:#1d201a;
  --light:#f2f2f2;
  --line:#e3e3e3;
  --white:#fff;
}
*{box-sizing:border-box;margin:0;padding:0}
html,body{width:1200px;height:4478px;overflow:hidden}
body{font-family:'Roboto',Arial,sans-serif;color:var(--text);background:var(--white);font-size:12px;line-height:1.6}
section,header,footer,nav{position:relative;width:1200px;overflow:hidden}
.abs{position:absolute}
.kicker{font-size:10px;font-weight:700;letter-spacing:1px;color:var(--gold);text-transform:uppercase}
.title{font-weight:900;color:var(--ink);text-transform:uppercase;font-size:32px;line-height:1.1}
.title.light{color:var(--white)}
.rule{width:40px;height:2px;background:var(--gold);margin:10px auto}
.center{text-align:center}
.lead{font-size:11.5px;color:var(--text);line-height:1.6}
.btn{display:inline-block;font-size:9.5px;font-weight:700;letter-spacing:.6px;text-transform:uppercase;padding:0 18px;height:28px;line-height:28px}
.btn.fill{background:var(--gold);color:var(--white)}
.btn.outline{border:1px solid var(--gold);color:var(--gold)}
.btn.outline-light{border:1px solid var(--gold);color:var(--white)}
.ph{display:block}
.topbar{height:30px;background:var(--dark-3);color:#ccc;font-size:10px}
.topbar .follow{left:233px;top:8px;display:flex;gap:8px;align-items:center}
.topbar .dot{width:7px;height:7px;background:#bbb;border-radius:50%}
.topbar .account{right:233px;top:8px}
.topbar .account b{color:var(--gold);font-weight:500}
.site-header{height:78px;background:var(--dark)}
.brand{left:233px;top:24px;display:flex;align-items:center;gap:12px}
.brand-mark{width:26px;height:26px;background:var(--gold)}
.brand-name{color:var(--gold);font-size:17px;font-weight:500;letter-spacing:.5px;text-transform:uppercase}
.contact-item{top:20px;display:flex;gap:8px;align-items:flex-start;color:#ccc;font-size:10px;line-height:1.4}
.contact-item strong{display:block;font-size:17px;color:var(--white);font-weight:700}
.contact-item.phone strong{color:var(--gold)}
.main-nav{height:35px;background:var(--gold)}
.main-nav ul{list-style:none;position:absolute;left:233px;top:0;display:flex;gap:32px;height:35px;align-items:center}
.main-nav li{color:var(--white);font-size:9.5px;font-weight:700;text-transform:uppercase}
.main-nav .donate{right:235px;top:5px;height:25px;line-height:23px;border:1px solid var(--white);color:var(--white);padding:0 26px;font-size:9.5px;font-weight:700}
.hero{height:520px}
.hero-photo{position:absolute;inset:0;background:linear-gradient(100deg,#4d5a3a 0%,#6d7650 35%,#4a4f3a 60%,#7a3b2d 85%,#3d4230 100%)}
.hero-shade{position:absolute;inset:0;background:rgba(20,24,16,.45)}
.hero-copy{position:absolute;left:0;right:0;top:160px;text-align:center;color:var(--white)}
.hero-copy h1{font-size:40px;font-weight:900;line-height:1.1;text-transform:uppercase;margin-top:6px}
.hero-copy p{width:460px;margin:14px auto 0;font-size:11px;line-height:1.6;color:#e8e8e8}
.hero-copy .btn{margin-top:22px}
.dots{display:flex;gap:8px;justify-content:center}
.dots i{width:6px;height:6px;border-radius:50%;background:#bbb;display:block}
.dots i.on{background:var(--gold)}
.activities{height:552px}
.act-head{position:absolute;top:70px;left:0;right:0}
.act-head .lead{width:560px;margin:0 auto}
.cards3{position:absolute;top:212px;left:233px;display:flex;gap:8px}
.act-card{width:240px;height:265px;border:1px solid var(--line);text-align:center;padding-top:38px}
.act-card h3{font-size:12.5px;color:var(--ink);font-weight:700;margin-top:14px}
.act-card h3.gold{color:var(--gold)}
.act-card p{width:170px;margin:8px auto 16px;font-size:10px;line-height:1.6}
.gallery{height:481px;background:var(--dark-2)}
.gallery-copy{left:233px;top:82px;width:345px}
.gallery-copy .title{font-size:30px;margin-top:4px}
.gallery-copy .rule{margin:10px 0}
.gallery-copy p{color:#cfcfcf;font-size:10.5px;line-height:1.6}
.thumb{top:218px;width:165px;height:120px}
.gallery .dots{left:233px;top:356px;justify-content:flex-start}
.gallery .btn{left:233px;top:378px}
.gallery-main{left:610px;top:75px;width:354px;height:332px}
.testimonials{height:325px}
.quotes{position:absolute;top:78px;left:233px;display:flex;gap:0}
.quote{width:245px;text-align:center}
.avatar{width:42px;height:42px;border-radius:50%;margin:0 auto;background:linear-gradient(#d9d4cc,#a9a39a)}
.quote h4{color:var(--gold);font-size:12px;font-weight:700;margin-top:12px}
.quote small{display:block;font-size:8px;font-weight:700;color:#555;letter-spacing:.6px}
.quote p{width:190px;margin:6px auto 0;font-size:10px;line-height:1.6}
.testimonials .dots{position:absolute;left:0;right:0;top:243px}
.blog{height:591px;background:var(--light)}
.blog-head{position:absolute;top:62px;left:0;right:0}
.blog-head .lead{width:560px;margin:0 auto}
.posts{position:absolute;top:207px;left:233px;display:flex;gap:8px}
.post{width:240px;background:var(--white)}
.post .ph{height:155px}
.post-body{height:153px;padding:14px 18px;text-align:center}
.post-meta{display:flex;justify-content:space-between;font-size:8px;font-weight:700;color:#555}
.post-meta b{color:var(--gold)}
.post h3{font-size:13.5px;font-weight:500;color:var(--ink);line-height:1.3;margin-top:10px}
.post h3.gold{color:var(--gold)}
.post p{font-size:10px;line-height:1.6;margin-top:10px}
.about{height:364px}
.about-photo{position:absolute;inset:0;background:linear-gradient(90deg,#8f9192 0%,#b7b9bc 20%,#7a3a38 40%,#3f4a44 62%,#263129 100%)}
.about-copy{left:670px;top:72px;width:300px;color:var(--white)}
.about-copy .title{font-size:32px;margin-top:4px}
.about-copy .rule{margin:10px 0}
.about-copy p{font-size:10.5px;line-height:1.6;color:#ddd}
.about-copy ol{list-style:none;margin-top:14px}
.about-copy li{font-size:11.5px;font-weight:500;line-height:1.75}
.about-copy li b{color:var(--gold);margin-right:6px}
.management{height:532px}
.team{position:absolute;top:160px;left:233px;display:flex;gap:18px}
.member{width:170px;border:1px solid var(--line);text-align:center}
.member .ph{height:168px}
.member h4{font-size:12px;color:var(--ink);font-weight:500;margin-top:14px}
.member small{display:block;color:var(--gold);font-size:8px;font-weight:700;letter-spacing:.6px}
.member .social{border-top:1px solid var(--line);margin-top:18px;height:36px;display:flex;justify-content:center;gap:16px;align-items:center}
.member .social i{width:7px;height:7px;background:#777;border-radius:50%;display:block}
.info-strip{height:131px;background:var(--dark-2)}
.info-col{top:0;height:131px;width:400px;text-align:center;padding-top:38px;color:var(--white)}
.info-col+.info-col{border-left:1px solid #41473a}
.info-col span{display:inline-block;border:1px solid var(--gold);color:var(--gold);font-size:9px;font-weight:700;padding:1px 12px;letter-spacing:.6px}
.info-col p{font-size:19px;margin-top:6px}
.contact{height:466px;background:#f4f4f2}
.contact-map{position:absolute;inset:0;opacity:.6}
.contact-head{position:absolute;top:64px;left:0;right:0}
.field{height:28px;border:1px solid #ddd;background:var(--white);font-size:9.5px;color:#555;padding:6px 12px}
.contact .btn{left:550px;top:368px}
.site-footer{height:343px;background:var(--dark-3);color:#bbb}
.foot-news{left:233px;top:90px;width:215px;text-align:center}
.foot-title{font-size:17px;font-weight:700;color:var(--white);text-transform:uppercase}
.foot-news p{font-size:10px;line-height:1.6;margin-top:12px}
.foot-news .input{height:30px;border:1px solid #666;margin-top:16px}
.foot-card{left:485px;top:38px;width:230px;height:260px;background:var(--white);text-align:center;padding-top:40px}
.foot-card .mark{width:30px;height:30px;background:var(--gold);margin:0 auto}
.foot-card h4{font-size:20px;font-weight:700;color:var(--ink);margin-top:8px}
.foot-card p{font-size:10px;line-height:1.6;width:160px;margin:10px auto 0;color:#666}
.foot-card .social{display:flex;gap:14px;justify-content:center;margin-top:14px}
.foot-card .social i{width:7px;height:7px;background:#555;border-radius:50%;display:block}
.foot-events{left:760px;top:90px;width:210px;text-align:center}
.foot-events h5{font-size:11px;color:var(--white);font-weight:700;margin-top:14px;line-height:1.4}
.foot-events .meta{display:flex;justify-content:center;gap:10px;font-size:8.5px;margin-top:4px}
.foot-events .meta b{color:var(--gold)}
.foot-events p{font-size:9.5px;line-height:1.5;color:#999}
.copyright{height:30px;background:var(--dark-3);border-top:1px solid #333;text-align:center;font-size:8.5px;line-height:30px;color:#888}
</style>
</head>
<body>

<div class="topbar">
  <div class="abs follow">Follow Us <i class="dot"></i><i class="dot"></i><i class="dot"></i><i class="dot"></i></div>
  <div class="abs account"><b>Register</b> &nbsp;|&nbsp; Login</div>
</div>

<header class="site-header">
  <div class="abs brand"><span class="brand-mark"></span><span class="brand-name">Kindred Harbor Network</span></div>
  <div class="abs contact-item phone" style="left:700px">
    <svg width="14" height="14" viewBox="0 0 24 24" fill="#c39a3e"><path d="M6.6 10.8a15 15 0 0 0 6.6 6.6l2.2-2.2a1 1 0 0 1 1-.25 11 11 0 0 0 3.6.6 1 1 0 0 1 1 1V20a1 1 0 0 1-1 1A17 17 0 0 1 3 4a1 1 0 0 1 1-1h3.5a1 1 0 0 1 1 1 11 11 0 0 0 .6 3.6 1 1 0 0 1-.25 1z"/></svg>
    <div><strong>0800 555 0192</strong>hello@kindredharbor.org</div>
  </div>
  <div class="abs contact-item" style="left:840px">
    <svg width="12" height="16" viewBox="0 0 24 32" fill="#c39a3e"><path d="M12 0a12 12 0 0 0-12 12c0 9 12 20 12 20s12-11 12-20A12 12 0 0 0 12 0zm0 17a5 5 0 1 1 0-10 5 5 0 0 1 0 10z"/></svg>
    <div><strong>2240 Alder Row</strong>Fairhaven, Oregon</div>
  </div>
</header>

<nav class="main-nav">
  <ul><li>Home</li><li>Rooms</li><li>Activities</li><li>Events</li><li>Gallery</li><li>Blog</li><li>Shop</li><li>Contact Us</li></ul>
  <div class="abs donate">DONATE</div>
</nav>

<section class="hero">
  <div class="hero-photo" role="img" aria-label="Photo of a family member embracing a child holding a small flag"></div>
  <div class="hero-shade"></div>
  <div class="hero-copy">
    <div class="kicker" style="color:#fff">Senior Living Advice</div>
    <h1>For those who care for<br>our seniors.</h1>
    <p>Every day you look after an aging parent or loved one. Our local advisors help you find the right senior living option, free of charge.</p>
    <span class="btn outline-light">Read More</span>
  </div>
  <div class="abs dots" style="left:0;right:0;top:480px"><i class="on"></i><i></i><i></i></div>
</section>

<section class="activities">
  <div class="act-head center">
    <div class="kicker">Find Support</div>
    <h2 class="title">Our Activities</h2>
    <div class="rule"></div>
    <p class="lead">Caring families find trusted senior living, daily programs and respite services close to home. Our advisors guide every step so loved ones stay safe and supported.</p>
  </div>
  <div class="cards3">
    <div class="act-card">
      <svg width="34" height="30" viewBox="0 0 34 30" fill="none" stroke="#333" stroke-width="1.6"><rect x="2" y="7" width="30" height="21" rx="2"/><path d="M12 7V3h10v4M17 12v11M11.5 17.5h11"/></svg>
      <h3>Rehabilitation</h3>
      <p>Our team of licensed therapists helps residents regain strength, mobility and daily confidence.</p>
      <span class="btn fill">Read More</span>
    </div>
    <div class="act-card">
      <svg width="34" height="30" viewBox="0 0 34 30" fill="none" stroke="#333" stroke-width="1.6"><path d="M17 12c-3-6-11-4-9 2 1 3 9 8 9 8s8-5 9-8c2-6-6-8-9-2z"/><path d="M3 26h9l5-3h8"/></svg>
      <h3 class="gold">Charity</h3>
      <p>Our advocates offer kind help to seniors and families facing the cost of care.</p>
      <span class="btn outline">Read More</span>
    </div>
    <div class="act-card">
      <svg width="34" height="30" viewBox="0 0 34 30" fill="none" stroke="#333" stroke-width="1.6"><rect x="3" y="8" width="28" height="20" rx="2"/><path d="M12 8V4h10v4M3 16h28M17 13v6"/></svg>
      <h3>Education</h3>
      <p>Helpful learning sessions ensure caregivers and residents keep growing together.</p>
      <span class="btn fill">Read More</span>
    </div>
  </div>
</section>

<section class="gallery">
  <div class="abs gallery-copy">
    <div class="kicker">What We Do</div>
    <h2 class="title light">Our Gallery</h2>
    <div class="rule"></div>
    <p>Moments from our communities show the friendship, pride and care shared every day. Residents, families and staff gather for celebrations, outings and quiet afternoons together.</p>
  </div>
  <div class="abs thumb ph" style="left:233px;background:linear-gradient(135deg,#7d3a33,#b9b3a3 50%,#4f5a3e)" role="img" aria-label="Photo of a resident saluting before a flag"></div>
  <div class="abs thumb ph" style="left:411px;background:linear-gradient(135deg,#6b7450,#a29a7c 55%,#4c5538)" role="img" aria-label="Photo of a resident hugging a family member"></div>
  <div class="abs dots"><i class="on"></i><i></i><i></i></div>
  <span class="abs btn outline-light">See All</span>
  <div class="abs gallery-main ph" style="background:linear-gradient(160deg,#9a3d36 0%,#c8c2b8 30%,#5a5f45 60%,#3d4230 100%)" role="img" aria-label="Photo of an elderly resident in dress uniform saluting before a flag"></div>
</section>

<section class="testimonials">
  <div class="quotes">
    <div class="quote"><div class="avatar" role="img" aria-label="Portrait of a resident"></div><h4>Owen Marsh</h4><small>RESIDENT</small><p>The advisor found my father a place near us within a week, and he is happier than he has been in years.</p></div>
    <div class="quote"><div class="avatar" role="img" aria-label="Portrait of a caregiver"></div><h4>Nina Carver</h4><small>CAREGIVER</small><p>An advisor listened to every concern and walked our family through each option with real patience.</p></div>
    <div class="quote"><div class="avatar" role="img" aria-label="Portrait of a resident"></div><h4>Helen Brook</h4><small>RESIDENT</small><p>I feel respected and at home here. The daily programs keep me busy and connected to friends.</p></div>
  </div>
  <div class="dots"><i class="on"></i><i></i><i></i></div>
</section>

<section class="blog">
  <div class="blog-head center">
    <div class="kicker">News &amp; Events</div>
    <h2 class="title">Our Blog</h2>
    <div class="rule"></div>
    <p class="lead">Guides, stories and updates for families exploring senior living. Learn what to ask, what to expect and how to support a loved one through every change.</p>
  </div>
  <div class="posts">
    <article class="post"><div class="ph" style="background:linear-gradient(135deg,#8e3b35,#c9c3bb 50%,#5b5f48)" role="img" aria-label="Photo of residents saluting with a flag"></div>
      <div class="post-body"><div class="post-meta"><span>JAN 06, 2018</span><b>CHARITY</b></div><h3>Helping a parent settle into a new home</h3><p>Simple ways to comfort a parent during the first weeks in a new home.</p></div></article>
    <article class="post"><div class="ph" style="background:linear-gradient(135deg,#6a5a44,#9b3a35 50%,#3f3a30)" role="img" aria-label="Photo of a senior holding a flag"></div>
      <div class="post-body"><div class="post-meta"><span>JAN 06, 2018</span><b>ASSISTANCE</b></div><h3 class="gold">How we match families with the right care</h3><p>What our advisors weigh when they suggest a care setting.</p></div></article>
    <article class="post"><div class="ph" style="background:linear-gradient(135deg,#9b3a35,#7a7360 45%,#2f3528)" role="img" aria-label="Photo of an elderly man in a cap"></div>
      <div class="post-body"><div class="post-meta"><span>JAN 06, 2018</span><b>CARE</b></div><h3>Questions to ask on a community tour</h3><p>A short checklist for visiting an assisted living community.</p></div></article>
  </div>
</section>

<section class="about">
  <div class="about-photo" role="img" aria-label="Photo of small flags planted in a row"></div>
  <div class="abs about-copy">
    <div class="kicker">About Us</div>
    <h2 class="title light">Who We Are</h2>
    <div class="rule"></div>
    <p>We are a free referral network helping seniors and their families find safe, caring homes. Local advisors know each community and stay with families from the first call to move-in day.</p>
    <ol>
      <li><b>01.</b>Assisted living referrals</li>
      <li><b>02.</b>Memory care guidance</li>
      <li><b>03.</b>In-home care options</li>
      <li><b>04.</b>Senior benefits advice</li>
    </ol>
  </div>
</section>

<section class="management">
  <div class="abs center" style="left:0;right:0;top:70px">
    <div class="kicker">Our Team</div>
    <h2 class="title">Management</h2>
    <div class="rule"></div>
  </div>
  <div class="team">
    <div class="member"><div class="ph" style="background:linear-gradient(#e8e2da,#b58a6a)" role="img" aria-label="Portrait of the director"></div><h4>Mara Ellison</h4><small>DIRECTOR</small><div class="social"><i></i><i></i><i></i></div></div>
    <div class="member"><div class="ph" style="background:linear-gradient(#e6e6e6,#4a4d55)" role="img" aria-label="Portrait of the manager"></div><h4>Peter Hale</h4><small>MANAGER</small><div class="social"><i></i><i></i><i></i></div></div>
    <div class="member"><div class="ph" style="background:linear-gradient(#efefef,#c9b59a)" role="img" aria-label="Portrait of the coordinator"></div><h4>Joan Pryor</h4><small>COORDINATOR</small><div class="social"><i></i><i></i><i></i></div></div>
    <div class="member"><div class="ph" style="background:linear-gradient(#f0f0f0,#6f8fae)" role="img" aria-label="Portrait of the volunteer"></div><h4>Grant Fellows</h4><small>VOLUNTEER</small><div class="social"><i></i><i></i><i></i></div></div>
  </div>
</section>

<section class="info-strip">
  <div class="abs info-col" style="left:0"><span>HEAD OFFICE</span><p>2240 Alder Row, Fairhaven</p></div>
  <div class="abs info-col" style="left:400px"><span>EMAIL US</span><p>hello@kindredharbor.org</p></div>
  <div class="abs info-col" style="left:800px"><span>CALL US</span><p>0800 555 0192</p></div>
</section>

<section class="contact">
  <div class="contact-map" role="img" aria-label="Faint street map background" style="background:linear-gradient(135deg,#f0f0ee,#e6e6e3 50%,#f2f2f0)"></div>
  <div class="contact-head center">
    <div class="kicker">Write Us</div>
    <h2 class="title">Contact Form</h2>
    <div class="rule"></div>
  </div>
  <div class="abs field" style="left:360px;top:150px;width:244px">Your Name</div>
  <div class="abs field" style="left:612px;top:150px;width:228px">Email Address</div>
  <div class="abs field" style="left:360px;top:190px;width:244px">Phone Number</div>
  <div class="abs field" style="left:612px;top:190px;width:228px">Your Subject</div>
  <div class="abs field" style="left:360px;top:230px;width:480px;height:108px">Your Message</div>
  <span class="abs btn outline">Send Message</span>
</section>

<footer class="site-footer">
  <div class="abs foot-news">
    <div class="foot-title">Newsletter</div>
    <p>Subscribe to our newsletter for care tips and news delivered to you.</p>
    <div class="input"></div>
  </div>
  <div class="abs foot-card">
    <div class="mark"></div>
    <h4>Kindred Harbor</h4>
    <p>A free network linking seniors and families with trusted local care homes and friendly advisors.</p>
    <div class="social"><i></i><i></i><i></i><i></i></div>
  </div>
  <div class="abs foot-events">
    <div class="foot-title">News &amp; Events</div>
    <h5>Family open house at our partner homes</h5>
    <div class="meta"><span><b>●</b> 10:00</span><span><b>●</b> ADMIN</span><span><b>●</b> NEWS</span></div>
    <p style="margin-top:14px">Free talk on paying for senior care</p>
    <div class="meta"><span><b>●</b> 17:00</span><span><b>●</b> ADMIN</span><span><b>●</b> NEWS</span></div>
  </div>
</footer>
<div class="copyright">COPYRIGHT © 2018</div>

</body>
</html>
```